Need a business card for our overland brand!

We had the logo made and we need a great design for our business card. Use the logo provide or tweak it however you see fit.

Contact Information for Business Card

Name, Title, Telephone, email, website

```html
<!DOCTYPE html>
<html lang="en">
<head>
<meta charset="utf-8">
<title>Summit Trail Overland – Business Card</title>
<link rel="stylesheet" href="https://fonts.googleapis.com/css2?family=Oswald:wght@600;700&family=Roboto:wght@400&display=swap">
<style>
  :root {
    --navy: #253a55;
    --navy-deep: #22354f;
    --cyan: #1a9fc4;
    --white: #ffffff;
    --silver: #d6dadf;
    --backdrop: #2c2c2c;
  }
  * { margin: 0; padding: 0; box-sizing: border-box; }
  html, body { width: 1200px; height: 895px; overflow: hidden; }
  body {
    background: var(--backdrop);
    font-family: "Roboto", Arial, sans-serif;
    position: relative;
  }
  .card {
    position: absolute;
    top: 150px;
    width: 340px;
    height: 595px;
    border-radius: 26px;
    overflow: hidden;
  }
  .card--front { left: 230px; background: var(--white); }
  .card--back { left: 630px; background: var(--navy); }

  .front__split { position: absolute; inset: 0; }

  .brand-name {
    position: absolute;
    font-family: "Oswald", "Arial Narrow", sans-serif;
    font-weight: 700;
    text-transform: uppercase;
    line-height: 0.95;
    letter-spacing: 0.5px;
  }
  .card--front .brand-name {
    top: 80px; right: 34px;
    color: var(--navy);
    font-size: 40px;
    text-align: right;
  }
  .card--back .brand-name {
    top: 310px; left: 0; right: 0;
    color: var(--silver);
    font-size: 48px;
    text-align: center;
  }

  .person {
    position: absolute;
    left: 34px; top: 380px;
    color: var(--white);
  }
  .person__name {
    font-family: "Oswald", "Arial Narrow", sans-serif;
    font-weight: 700;
    font-size: 27px;
    color: var(--cyan);
    text-transform: uppercase;
    letter-spacing: 0.5px;
    line-height: 1.1;
  }
  .person__title { font-size: 15px; margin-top: 4px; }
  .person__rule {
    width: 86px; height: 3px;
    background: var(--cyan);
    margin: 14px 0 16px;
  }
  .contact { list-style: none; font-size: 13px; }
  .contact li {
    display: flex; align-items: center; gap: 9px;
    margin-bottom: 9px;
  }
  .contact svg { width: 14px; height: 14px; flex: none; }
</style>
</head>
<body>

<section class="card card--front">
  <svg class="front__split" viewBox="0 0 340 595" aria-hidden="true">
    <polygon points="0,272 340,318 340,595 0,595" fill="var(--cyan)"/>
    <polygon points="0,282 340,328 340,595 0,595" fill="var(--navy)"/>
  </svg>

  <div class="brand-name">Summit Trail<br>Overland</div>

  <div class="person">
    <div class="person__name">Dana Whitfield</div>
    <div class="person__title">Founder and CEO</div>
    <div class="person__rule"></div>
    <ul class="contact">
      <li>
        <svg viewBox="0 0 16 16" aria-hidden="true"><path d="M4 1.5 6.3 4 5 5.6c.8 1.9 2.3 3.4 4.2 4.3l1.5-1.3L13.5 11 12 13.8C6.8 13.3 2.7 9.2 2.2 4Z" fill="var(--cyan)"/></svg>
        000 000 0000
      </li>
      <li>
        <svg viewBox="0 0 16 16" aria-hidden="true"><rect x="1.5" y="3.5" width="13" height="9" rx="1" fill="var(--cyan)"/><path d="M1.8 4 8 9l6.2-5" fill="none" stroke="var(--navy)" stroke-width="1.2"/></svg>
        info@summittrailoverland.com
      </li>
      <li>
        <svg viewBox="0 0 16 16" aria-hidden="true"><circle cx="8" cy="8" r="6.5" fill="none" stroke="var(--cyan)" stroke-width="1.4"/><ellipse cx="8" cy="8" rx="2.8" ry="6.5" fill="none" stroke="var(--cyan)" stroke-width="1.2"/><path d="M1.5 8h13M2.5 5h11M2.5 11h11" stroke="var(--cyan)" stroke-width="1"/></svg>
        www.summittrailoverland.com
      </li>
    </ul>
  </div>
</section>

<section class="card card--back">
  <div class="brand-name">Summit Trail<br>Overland</div>
</section>

</body>
</html>
```